Etiketten-Design für Gin gesucht
Wahnsinnige Arbeit die Henrike hier abgeliefert hat. Es wurde nicht nur ein Etikett sondern ein Design für eine ganze Produkt-Linie erstellt. Bereits mit dem ersten Design war dies eines unserer Top-Designs und wurde dann perfekt weiterentwickelt. Viele Grüße und Danke für die super Zusammenarbeit. Tobias, Lutz, Sepp
Zielgruppe
Habadere.
Wir sind ein Team aus drei bayerischen Hobby Brennern und werden unter der Marke 'Feld Brennerei' Anfang 2021 einen GIN auf den Markt bringen.
Der GIN wird schwerpunktmäßig online verkauft und sollte daher eine exklusiv-auffällige Optik haben um die Kunden zu beeindrucken.
Unsere Spirituosen erweitern traditionelle Rezepte mit regionalen Zutaten und bringen dies mit ihrer stilvollen Verpackung zum Ausdruck. Unser GIN ist eine Entdeckung für Leute, die schon alles kennen und Spirituosen auch pur genießen ohne Tonic oder andere Mixgetränke. Wir legen sehr viel Wert auf Qualität der Zutaten sowie Zeit und Geduld im Herstellungsprozess. Durch die handwerkliche Kunst des Destillierens bieten wir immer neue Erlebnisse für den Feinschmecker in kleinen limitieren Losgrößen.
So kommt es, dass wir Sonntags rund um den Stillen Horn (Oberbach am Horn - 97321) spazieren, dabei immer auf der Jagd nach neuen Zutaten sind und diese dem traditionellen Wacholder hinzufügen.
Im Gegensatz zu vielen anderen GIN Sorten, die weit über 30 Botanicals verwenden, setzen wir eine reduzierte Auswahl von maximal zehn zusätzlichen Zutaten ein, damit Kunden diesen puren und unverwechselbaren Geschmack genießen können (z.B. rosa Pfeffer, Korriander, Zitrone etc.). Zu Beginn besteht die Marke aus drei verschiedenen GIN Sorten und wird später um weitere Spirituosen wie Geiste und alkoholische Mischgetränke sowie Tonics erweitert. Auch Gläser und Merchandise Artikel soll es von uns geben. Jede GIN und Geist Variante besticht durch eine besondere Zutat, die Botanicals in unseren Spirituosen sind ohnehin auf wenige beschränkt, wodurch wir jedem Getränk eine besondere Note und einen speziellen Charakter verleihen.
Aufgabenstellung
Wir suchen ein GIN-Etikett dessen Design ausdrückt, dass es sich um einen handgemachten, hochwertigen und limitierten GIN handelt. Wir sind offen für puristische Entwürfe als auch für kreativ-künstlerische Ideen die auf die Flasche gebracht werden können.
Unser erster GIN wird den Namen „gold“ tragen, vielleicht kann man es geschrieben oder aber auch als „X“ für die römische zehn einbauen.
Vorschläge sind nicht auf ein einzelnes Etikett beschränkt, das Haupt-Etikett darf auch in verschiedene Abschnitte unterteilt werden, wie es in den Anlagen bspw. zu sehen ist. Zudem freuen wir uns über Entwürfe zum Etikett der Flaschenrückseite sowie den Flaschenhals.
Da weitere Spirituosen (nicht nur GIN) folgen, soll das Etikett einen großen Wiedererkennungswert haben und sich bspw. der Spirituosen-Name einfach austauschen lassen oder sich 'nur' durch individuelle Farbgebung unterscheiden.
Je nach Umsetzung können Etiketten im Folientransferdruck hergestellt werden. Unser Logo kann, muss aber nicht zwangsläufig auf dem Hauptetikett zu finden sein.
Unser Schwerpunkt liegt regional in Bayreuth, Tafelland Frankenhöhe und am Stillen Horn (97321 Oberbach am Horn).
Es darf in das Etikett auch gerne eine Art „Skala“, hinten oder vorne eingebaut werden, je nach Design für bestimmte Ausprägung der Geschmacksrichtung, hier die folgenden Kategorien und in der Anlage ist auch ein Beispiel zu finden.
Kategorien
Wacholder, blumig, fruchtig, würzig

```html
<!DOCTYPE html>
<html lang="de">
<head>
<meta charset="utf-8">
<title>Feld Brennerei – Etiketten</title>
<link rel="stylesheet" href="https://fonts.googleapis.com/css2?family=Jost:wght@300;400;700;900&family=Oswald:wght@300&family=Nanum+Pen+Script&display=swap">
<style>
  :root {
    --bg: #f3f3f3;
    --label: #ffffff;
    --band: #f0f0f0;
    --mark: #d5d5d5;
    --muted: #777777;
    --ink: #555555;
    --gin: #7c3869;
    --gin-soft: #c7a4c0;
    --coffee: #4f2a27;
    --coffee-soft: #d4c2a3;
  }
  * { box-sizing: border-box; margin: 0; padding: 0; }
  html, body { width: 1156px; height: 1200px; overflow: hidden; }
  body {
    background: var(--bg);
    font-family: "Jost", "Futura", sans-serif;
    display: flex;
    justify-content: center;
    gap: 60px;
    padding-top: 50px;
  }
  .product { width: 460px; display: flex; flex-direction: column; align-items: center; }
  .gin { --accent: var(--gin); --accent-soft: var(--gin-soft); }
  .coffee { --accent: var(--coffee); --accent-soft: var(--coffee-soft); }

  /* neck label */
  .neck-label {
    width: 150px;
    background: var(--label);
    padding: 8px 14px 10px;
    text-align: center;
    margin-bottom: 36px;
    box-shadow: 0 1px 3px rgba(0,0,0,.08);
  }
  .neck-caption {
    font-family: "Oswald", sans-serif;
    font-weight: 300;
    font-size: 8px;
    color: var(--muted);
    line-height: 1.2;
  }
  .neck-field {
    background: var(--accent-soft);
    font-family: "Nanum Pen Script", cursive;
    font-size: 20px;
    line-height: 18px;
    height: 18px;
    color: #2a2a2a;
    margin-bottom: 5px;
  }
  .neck-field:last-child { margin-bottom: 0; }

  /* front label */
  .front-label {
    position: relative;
    width: 460px;
    height: 860px;
    background: var(--label);
    overflow: hidden;
    box-shadow: 0 1px 4px rgba(0,0,0,.08);
  }
  .product-name {
    position: absolute;
    top: 52px;
    right: 30px;
    font-size: 21px;
    letter-spacing: 0.5em;
    color: var(--accent);
    white-space: nowrap;
  }
  .product-name b { font-weight: 700; }
  .product-name span { font-weight: 300; }
  .brand-mark {
    position: absolute;
    top: 72px;
    left: 40px;
    font-weight: 900;
    font-size: 232px;
    line-height: 0.82;
    letter-spacing: -8px;
    color: var(--mark);
    white-space: nowrap;
  }
  .brand-sub {
    position: absolute;
    top: 470px;
    right: 26px;
    text-align: right;
  }
  .brand-sub strong {
    display: block;
    font-size: 22px;
    font-weight: 700;
    letter-spacing: 0.42em;
    color: var(--accent);
  }
  .brand-sub em {
    display: block;
    font-style: normal;
    font-weight: 300;
    font-size: 20px;
    letter-spacing: 0.4em;
    color: var(--coffee);
    margin-top: 2px;
  }
  .taste-scale { position: absolute; top: 520px; left: 60px; }
  .taste-scale text {
    font-family: "Jost", sans-serif;
    font-weight: 300;
    font-size: 11px;
    fill: var(--muted);
    letter-spacing: -0.02em;
  }
  .volume-band {
    position: absolute;
    left: 0; right: 0;
    bottom: 60px;
    height: 120px;
    background: var(--band);
    display: flex;
    align-items: center;
    justify-content: center;
    gap: 18px;
    font-family: "Oswald", sans-serif;
    font-weight: 300;
    font-size: 28px;
    color: var(--ink);
  }
</style>
</head>
<body>

  <section class="product gin">
    <div class="neck-label">
      <p class="neck-caption">Batch No.</p>
      <p class="neck-field">003/166</p>
      <p class="neck-caption">Date of Distillation</p>
      <p class="neck-field">12/2020</p>
      <p class="neck-caption">Hand bottled for</p>
      <p class="neck-field">Anton Weber</p>
    </div>
    <div class="front-label">
      <h1 class="product-name"><b>GOLD</b><span>DRY</span><b>GIN</b></h1>
      <div class="brand-mark">FE<br>LD</div>
      <div class="brand-sub"><strong>BRENNEREI</strong></div>
      <svg class="taste-scale" width="340" height="120" viewBox="0 0 340 120">
        <g stroke="#999" stroke-width="1" fill="#fff">
          <line x1="80" y1="14" x2="240" y2="14"/>
          <line x1="80" y1="44" x2="240" y2="44"/>
          <line x1="80" y1="74" x2="240" y2="74"/>
          <line x1="80" y1="104" x2="240" y2="104"/>
        </g>
        <g stroke="#999" stroke-width="1" fill="#fff">
          <circle cx="80" cy="14" r="5.5"/><circle cx="120" cy="14" r="5.5"/><circle cx="160" cy="14" r="5.5"/><circle cx="200" cy="14" r="5.5"/>
          <circle cx="80" cy="44" r="5.5"/><circle cx="160" cy="44" r="5.5"/><circle cx="200" cy="44" r="5.5"/><circle cx="240" cy="44" r="5.5"/>
          <circle cx="80" cy="74" r="5.5"/><circle cx="120" cy="74" r="5.5"/><circle cx="160" cy="74" r="5.5"/><circle cx="240" cy="74" r="5.5"/>
          <circle cx="80" cy="104" r="5.5"/><circle cx="120" cy="104" r="5.5"/><circle cx="200" cy="104" r="5.5"/><circle cx="240" cy="104" r="5.5"/>
        </g>
        <g fill="var(--gin)">
          <circle cx="240" cy="14" r="6"/>
          <circle cx="120" cy="44" r="6"/>
          <circle cx="200" cy="74" r="6"/>
          <circle cx="160" cy="104" r="6"/>
        </g>
        <text x="0" y="18">WACHOLDER</text>
        <text x="0" y="48">FLORAL</text>
        <text x="0" y="78">FRUCHTIG</text>
        <text x="0" y="108">GEWÜRZE</text>
      </svg>
      <div class="volume-band"><span>700ml</span><span>Alc. 43%vol.</span></div>
    </div>
  </section>

  <section class="product coffee">
    <div class="neck-label">
      <p class="neck-caption">Batch No.</p>
      <p class="neck-field">003/166</p>
      <p class="neck-caption">Date of Distillation</p>
      <p class="neck-field">12/2020</p>
      <p class="neck-caption">Hand bottled for</p>
      <p class="neck-field">Anton Weber</p>
    </div>
    <div class="front-label">
      <h1 class="product-name"><b>KAFFEE</b><span>GEIST</span></h1>
      <div class="brand-mark">FE<br>LD</div>
      <div class="brand-sub"><strong>BRENNEREI</strong><em>100% ARABICA</em></div>
      <div class="volume-band"><span>700ml</span><span>Alc. 43%vol.</span></div>
    </div>
  </section>

</body>
</html>
```